Modern Design Business Card industrial maintenance company

Business card design for Company named Brookvale Equipment Services

Target Market(s)

Industrial

Industry/Entity Type

Maintenance and repair

Contact Information for Business Card

Place holder for address, office phone, mobile number and email

Requirements
Must have
• Clean modern look
Nice to have
• N/a

```html
<!DOCTYPE html>
<html lang="en">
<head>
<meta charset="utf-8">
<title>Brookvale Equipment Services – Business Card</title>
<link href="https://fonts.googleapis.com/css2?family=Lato:wght@400;700;900&display=swap" rel="stylesheet">
<style>
  :root {
    --backdrop: #3b3b3b;
    --card: #1c1c1c;
    --ink: #f2f2f2;
    --ink-soft: #d6d6d6;
    --rule: #e8e8e8;
    --silver: #c9c9c9;
  }
  * { box-sizing: border-box; margin: 0; padding: 0; }
  html, body {
    width: 1200px; height: 919px; overflow: hidden;
    background: var(--backdrop);
    font-family: "Lato", sans-serif;
    color: var(--ink);
  }
  .canvas {
    position: relative; width: 1200px; height: 919px;
    display: flex; align-items: center; justify-content: center; gap: 50px;
  }
  .card {
    position: relative; width: 520px; height: 310px;
    background: var(--card); border-radius: 26px;
    box-shadow: 0 18px 40px rgba(0,0,0,.35);
    overflow: hidden;
  }
  /* Front */
  .holder { position: absolute; left: 40px; top: 132px; }
  .holder-name { font-weight: 900; font-size: 25px; line-height: 30px; letter-spacing: .3px; text-transform: uppercase; }
  .holder-title { font-size: 13px; line-height: 17px; color: var(--ink-soft); margin-top: 1px; }
  .divider {
    position: absolute; left: 40px; top: 190px; width: 408px; height: 1px;
    background: var(--rule);
  }
  .contact { position: absolute; left: 30px; top: 208px; list-style: none; font-size: 12.5px; color: var(--ink-soft); }
  .contact li { display: flex; align-items: center; gap: 8px; line-height: 19px; }
  .contact svg { width: 10px; height: 10px; flex: none; }
  .front-brand {
    position: absolute; left: 362px; top: 24px; width: 140px;
    display: flex; flex-direction: column; align-items: center; gap: 8px; text-align: center;
  }
  .brand-dot { display: block; width: 96px; height: 96px; border: 4px solid var(--ink); border-radius: 50%; }
  .front-brand .brand-name { font-size: 12px; font-weight: 700; line-height: 15px; }
  .address {
    position: absolute; right: 56px; top: 236px; text-align: right;
    font-size: 12.5px; line-height: 18px; color: var(--ink-soft);
  }
  /* Back */
  .back-brand {
    position: absolute; inset: 0;
    display: flex; align-items: center; justify-content: center; gap: 22px;
  }
  .back-brand .brand-dot { width: 96px; height: 96px; border-color: var(--silver); order: 2; }
  .back-brand .brand-name {
    font-size: 24px; font-weight: 700; line-height: 1.2; color: var(--silver);
    text-transform: uppercase; letter-spacing: 1px; text-align: right;
  }
</style>
</head>
<body>
<main class="canvas">
  <section class="card card-front">
    <div class="front-brand">
      <span class="brand-dot"></span>
      <span class="brand-name">Brookvale Equipment Services</span>
    </div>
    <div class="holder">
      <h1 class="holder-name">Daniel Harper</h1>
      <p class="holder-title">Managing Director</p>
    </div>
    <div class="divider"></div>
    <ul class="contact">
      <li><svg viewBox="0 0 10 10"><path d="M2 1l2 2-1 1.2a5 5 0 0 0 2.8 2.8L7 6l2 2-1.2 1.4C4.5 9 1 5.5.6 2.2z" fill="currentColor"/></svg>(123) 456-7890</li>
      <li><svg viewBox="0 0 10 10"><rect x="2.5" y=".5" width="5" height="9" rx="1" fill="none" stroke="currentColor"/></svg>(123) 456-7890</li>
      <li><svg viewBox="0 0 10 10"><rect x=".5" y="2" width="9" height="6" fill="currentColor"/><path d="M.5 2L5 5.5 9.5 2" stroke="#1c1c1c" fill="none"/></svg>info@brookvaleequipment.com</li>
      <li><svg viewBox="0 0 10 10"><circle cx="5" cy="5" r="4.5" fill="currentColor"/></svg>brookvaleequipment.com</li>
    </ul>
    <p class="address">Your Address, City<br>State, Contry, Zip 1235</p>
  </section>

  <section class="card card-back">
    <div class="back-brand">
      <span class="brand-dot"></span>
      <span class="brand-name">Brookvale<br>Equipment Services</span>
    </div>
  </section>
</main>
</body>
</html>
```